Real Estate Flyer (Brenton Property)

We need a color CMYK high resolution, print quality horizontal real estate property flyer designed in the sizes of 10" wide and 6.7425" tall and another one in 11" wide and 8.5" tall.
Ad should be professionally looking to U.S. standards. It should be sleek, modern yet classy.
We uploaded in Briefs logo files, agent photo, 2 photos of the property (Must use both) and a sample of a flyer for Vayle Morrow Luxury Residence. We like how the overlay atop the first photo in the Vayle Morrow flyer with the company logo in the overlay. We'd like to incorporate that with our logo, the background color of the overlay should match that of our logo. DON'T CHANGE LOGO COLORS. Only use two colors in ad (exact logo blue color and white). The text in the overlay must be "FOR SALE - Potential Income Producing Commercial Office Building". Other details that should be prominent underneath are "42 Brenton Dr., Schaumburg, IL 60174 - Asking Price: $650,000".
Add "Residential & Commercial" under our company logo in italic font.
Add in flyer: "Located seconds away from the Kettering Rd. & Palden Rd. Intersection"
Add in flyer:
- Completely vacant
- 10,000 sq. ft. building
- 55 Car Parking
- 1.38 acre lot
- Over 20 offices and 5 bathrooms.
- Lease out individual office spaces for great monthly cash flow
Put agent's photo and following details professionally displayed:
Dev Marlo
Managing Broker
847-555-0148
dev.marlo@qtnhomes-example.com
Add from Briefs fair housing logo and PLX logo near agent's information. Logos should be small but yet visible to understand text.
Add at bottom of the ad with separation near agent details:
Looking to Buy or Sell?
I’m your one-stop, full service licensed real estate broker.
I deal with all types of real estate properties: Homes, Condos, Townhomes, Multi-Unit Apartment Buildings and Commercial Spaces.
Let My Experience Guide You Through Every Step of the Process!
Fine print:
©2018 QTN Homes, Inc. All Rights Reserved.

```html
<!DOCTYPE html>
<html lang="en">
<head>
<meta charset="utf-8">
<title>Brenton Property – Real Estate Flyer</title>
<link rel="stylesheet" href="https://fonts.googleapis.com/css2?family=Marcellus+SC&family=Arimo:ital,wght@0,400;0,700;1,400&display=swap">
<style>
  :root{
    --brand-blue:#1d44a0;
    --white:#ffffff;
    --board:#d9dadc;
    --board-edge:#c4c6c9;
    --label:#ffffff;
    --ink-soft:#5a6b8f;
    --sky-top:#b9cde3;
    --sky-bottom:#e6e9ec;
    --lawn:#6f7f52;
    --facade:#d8cdb8;
  }
  *{box-sizing:border-box;margin:0;padding:0}
  html,body{width:811px;height:1200px;overflow:hidden}
  body{
    background:radial-gradient(ellipse at 50% 40%, #eceeef 0%, var(--board) 60%, var(--board-edge) 100%);
    font-family:"Arimo", Arial, sans-serif;
    position:relative;
  }
  .size-label{
    position:absolute;left:60px;
    font-size:15px;color:var(--label);
    text-shadow:0 1px 2px rgba(0,0,0,.25);
  }
  .size-label--compact{top:28px}
  .size-label--letter{top:606px}

  .flyer{
    position:absolute;left:81px;width:676px;background:var(--white);
    box-shadow:0 3px 10px rgba(0,0,0,.25);overflow:hidden;
    display:flex;flex-direction:column;
  }
  .flyer--compact{top:62px;height:456px;--hero-h:176px;--band-h:118px;--s:1}
  .flyer--letter{top:640px;height:522px;--hero-h:206px;--band-h:136px;--s:1.08}

  .hero{
    height:var(--hero-h);flex:none;
    background:
      linear-gradient(180deg, transparent 62%, var(--lawn) 62%, #58663f 100%),
      linear-gradient(90deg, transparent 8%, var(--facade) 8%, #cfc3ad 70%, transparent 70%),
      linear-gradient(180deg, var(--sky-top), var(--sky-bottom));
  }

  .band{
    height:var(--band-h);flex:none;background:var(--brand-blue);color:var(--white);
    position:relative;padding:8px 0 0 0;text-align:center;
  }
  .band__copy{width:68%}
  .band__status{font-size:calc(32px * var(--s));font-weight:400;letter-spacing:1px;line-height:1.05}
  .band__headline{font-family:"Marcellus SC",serif;font-weight:400;font-size:calc(19px * var(--s));line-height:1.15;letter-spacing:.5px}
  .band__address{font-family:"Marcellus SC",serif;font-size:calc(10.5px * var(--s));margin-top:5px;letter-spacing:.3px}

  .brand{
    position:absolute;right:40px;top:-24px;width:128px;text-align:center;
  }
  .brand__mark{
    background:var(--brand-blue);border:2px solid var(--white);
    padding:calc(16px * var(--s)) 6px;display:flex;align-items:center;justify-content:center;gap:7px;
  }
  .brand__square{width:11px;height:11px;background:var(--white);flex:none}
  .brand__name{font-weight:700;font-size:calc(17px * var(--s));color:var(--white);white-space:nowrap}
  .brand__tagline{font-style:italic;font-size:calc(10px * var(--s));margin-top:5px;white-space:nowrap}

  .details{flex:1;min-height:0;display:flex;flex-direction:column;padding:9px 14px 4px 22px}
  .details__main{flex:1;min-height:0;display:flex;gap:14px}
  .details__left{width:52%}
  .location{
    font-family:"Marcellus SC",serif;color:var(--brand-blue);
    font-size:calc(11.5px * var(--s));line-height:1.2;
  }
  .feature-row{display:flex;gap:12px;margin-top:calc(7px * var(--s));align-items:flex-start}
  .feature-photo{
    width:calc(118px * var(--s));height:calc(70px * var(--s));flex:none;
    background:linear-gradient(180deg,var(--sky-top) 0%,var(--facade) 45%,var(--lawn) 100%);
  }
  .features{list-style:none;font-size:calc(8.2px * var(--s));color:var(--brand-blue);line-height:1.3}
  .features li{display:flex;gap:5px}
  .features li::before{content:"";width:4px;height:4px;background:var(--brand-blue);border-radius:50%;margin-top:4px;flex:none}

  .details__right{flex:1;display:flex;flex-direction:column;gap:6px}
  .agent{display:flex;gap:10px;align-items:flex-start}
  .agent__photo{
    width:calc(50px * var(--s));height:calc(58px * var(--s));flex:none;
    background:linear-gradient(180deg,#c9d2dc,#8b97a6);
  }
  .agent__info{color:var(--brand-blue);font-size:calc(7.8px * var(--s));line-height:1.35}
  .agent__name{font-family:"Marcellus SC",serif;font-size:calc(11.5px * var(--s))}
  .badges{display:flex;gap:6px;margin-left:auto;align-self:flex-start}
  .badge{width:20px;height:20px;border:1.5px solid var(--brand-blue)}
  .pitch{
    background:var(--brand-blue);color:var(--white);
    font-size:calc(7px * var(--s));line-height:1.35;padding:5px 8px;
  }
  .pitch p + p{margin-top:2px}
  .fine-print{
    flex:none;text-align:center;margin-top:3px;
    font-size:6px;color:var(--ink-soft);
  }
</style>
</head>
<body>

<p class="size-label size-label--compact">flyer size 10" x 6.7425"</p>
<article class="flyer flyer--compact">
  <div class="hero" role="img" aria-label="Photo of the two-storey office building at 42 Brenton Dr. with front lawn and parking"></div>
  <section class="band">
    <div class="band__copy">
      <h1 class="band__status">FOR SALE</h1>
      <h2 class="band__headline">Potential Income Producing<br>Commercial Office Building</h2>
      <p class="band__address">42 Brenton Dr., Schaumburg, IL 60174 – Asking Price: $650,000</p>
    </div>
    <div class="brand">
      <div class="brand__mark"><span class="brand__square"></span><span class="brand__name">QTN Homes</span></div>
      <p class="brand__tagline">Residential &amp; Commercial</p>
    </div>
  </section>
  <section class="details">
    <div class="details__main">
      <div class="details__left">
        <p class="location">Located seconds away from the Kettering Rd. &amp; Palden Rd. Intersection</p>
        <div class="feature-row">
          <div class="feature-photo" role="img" aria-label="Second view of the office building and parking lot"></div>
          <ul class="features">
            <li>Completely vacant</li>
            <li>10,000 sq. ft. building</li>
            <li>55 Car Parking</li>
            <li>1.38 acre lot</li>
            <li>Over 20 offices and 5 bathrooms</li>
            <li>Lease out individual office spaces for great monthly cash flow</li>
          </ul>
        </div>
      </div>
      <div class="details__right">
        <div class="agent">
          <div class="agent__photo" role="img" aria-label="Portrait of agent Dev Marlo"></div>
          <div class="agent__info">
            <p class="agent__name">Dev Marlo</p>
            <p>Managing Broker</p>
            <p>847-555-0148</p>
            <p>dev.marlo@qtnhomes-example.com</p>
          </div>
          <div class="badges"><span class="badge"></span><span class="badge"></span></div>
        </div>
        <div class="pitch">
          <p>Looking to Buy or Sell? I’m your one-stop, full service licensed real estate broker.</p>
          <p>I deal with all types of real estate properties: Homes, Condos, Townhomes, Multi-Unit Apartment Buildings and Commercial Spaces.</p>
          <p>Let My Experience Guide You Through Every Step of the Process!</p>
        </div>
      </div>
    </div>
    <p class="fine-print">©2018 QTN Homes, Inc. All Rights Reserved.</p>
  </section>
</article>

<p class="size-label size-label--letter">flyer size 11" x 8.5"</p>
<article class="flyer flyer--letter">
  <div class="hero" role="img" aria-label="Photo of the two-storey office building at 42 Brenton Dr. with front lawn and parking"></div>
  <section class="band">
    <div class="band__copy">
      <h1 class="band__status">FOR SALE</h1>
      <h2 class="band__headline">Potential Income Producing<br>Commercial Office Building</h2>
      <p class="band__address">42 Brenton Dr., Schaumburg, IL 60174 – Asking Price: $650,000</p>
    </div>
    <div class="brand">
      <div class="brand__mark"><span class="brand__square"></span><span class="brand__name">QTN Homes</span></div>
      <p class="brand__tagline">Residential &amp; Commercial</p>
    </div>
  </section>
  <section class="details">
    <div class="details__main">
      <div class="details__left">
        <p class="location">Located seconds away from the Kettering Rd. &amp; Palden Rd. Intersection</p>
        <div class="feature-row">
          <div class="feature-photo" role="img" aria-label="Second view of the office building and parking lot"></div>
          <ul class="features">
            <li>Completely vacant</li>
            <li>10,000 sq. ft. building</li>
            <li>55 Car Parking</li>
            <li>1.38 acre lot</li>
            <li>Over 20 offices and 5 bathrooms</li>
            <li>Lease out individual office spaces for great monthly cash flow</li>
          </ul>
        </div>
      </div>
      <div class="details__right">
        <div class="agent">
          <div class="agent__photo" role="img" aria-label="Portrait of agent Dev Marlo"></div>
          <div class="agent__info">
            <p class="agent__name">Dev Marlo</p>
            <p>Managing Broker</p>
            <p>847-555-0148</p>
            <p>dev.marlo@qtnhomes-example.com</p>
          </div>
          <div class="badges"><span class="badge"></span><span class="badge"></span></div>
        </div>
        <div class="pitch">
          <p>Looking to Buy or Sell? I’m your one-stop, full service licensed real estate broker.</p>
          <p>I deal with all types of real estate properties: Homes, Condos, Townhomes, Multi-Unit Apartment Buildings and Commercial Spaces.</p>
          <p>Let My Experience Guide You Through Every Step of the Process!</p>
        </div>
      </div>
    </div>
    <p class="fine-print">©2018 QTN Homes, Inc. All Rights Reserved.</p>
  </section>
</article>

</body>
</html>
```